Tinker's Fox sports bar beer & food menu

We need a menu design for our gastropub sports bar in L.A.'s Sawtelle Neighborhood (Little Osaka). We have a full-bar (hard liquor, craft beer, wine and cocktails) . We have a lunch and dinner menu as well as a happy hour menu. On Sundays we have a seperate menu with brunch items. The design concept is a British pub type of sports bar. We're looking for something different from our existing menu design. Ideally something cleaner and more legible. It should mesh a simple, modern sensibility with the more traditional darkened pub style of our interior design.

You can check out our Venuvista page for photos of the interior/exterior:
https://www.venuvista.com/biz_photos/tinkers-fox-los-angeles?tab=interior

You can view our existing menu here:
https://www.venuvista.com/biz_photos/tinkers-fox-los-angeles?tab=menu

If there's an area of the design that can be a little more playful it's our highlighted event schedule so that the events will stand out.

Target Market(s)

Age of 25 and up. Sawtelle is a cultural hub that caters to a younger, moderately affluent crowd.

Industry/Entity Type

Sports Bar

Font styles to use
Sans Serif

Colors

Designer to choose colors to be used in the design.

Requirements
Must have
• Logo, highlighted event schedule (beer pong Monday, trivia Tuesday, taco Tuesday, whiskey Wednesday, karaoke Saturday). The menu should be easy to read in a darkened bar. We'll be printing on standard 8.5x11 in portrait.
Nice to have
• We're trying to have the menu take up as few pages as possible.
Should not have
• We're trying to have the menu take up as few pages as possible. Food photography isn't necessary. A cover isn't necessary. Please avoid clip art of food.

```html
<!DOCTYPE html>
<html lang="en">
<head>
<meta charset="utf-8">
<title>Tinker's Fox — Pub &amp; Restaurant Menu</title>
<link href="https://fonts.googleapis.com/css2?family=Montserrat:wght@500;600;700&family=Crimson+Text:wght@400;600&display=swap" rel="stylesheet">
<style>
:root{
  --page:#e9e9e9;
  --bg-dark:#2c2926;
  --bg-mid:#3a3531;
  --gold:#f2a51f;
  --band:#a57b2c;
  --tile:#3b342c;
  --ink:#f5f2ec;
  --rule:#cfcac3;
  --sans:'Montserrat',Arial,sans-serif;
  --serif:'Crimson Text',Georgia,serif;
}
*{margin:0;padding:0;box-sizing:border-box}
html,body{width:1200px;height:1200px;overflow:hidden;background:var(--page)}
.menu{position:absolute;left:175px;top:0;width:850px;height:1200px;overflow:hidden;color:var(--ink);font-family:var(--sans)}
.menu__backdrop{position:absolute;inset:0;background:linear-gradient(180deg,#34302c 0%,#2a2724 45%,#3a342d 80%,#2d2925 100%)}
.brand{position:absolute;left:315px;top:14px;width:224px;height:60px;border-radius:30px;background:#8f8a86;display:flex;align-items:center;justify-content:center;gap:10px}
.brand__dot{width:16px;height:16px;border-radius:50%;background:var(--bg-dark)}
.brand__name{font-family:var(--sans);font-weight:700;font-size:22px;color:var(--bg-dark)}
.section{position:absolute;border:2px solid var(--rule);padding:24px 18px 0 22px}
.section__title{position:absolute;top:-11px;left:14px;padding:0 8px;background:var(--bg-dark);color:var(--gold);font-weight:700;font-size:17px;line-height:20px;letter-spacing:.2px}
.item{margin-bottom:7px}
.item__name{font-weight:700;font-size:14.5px;line-height:16px}
.item__desc{font-family:var(--serif);color:var(--gold);font-size:10.5px;line-height:11px}
.item__name small{font-size:11px;font-weight:600}
.upper .item__name{text-transform:uppercase}
.upper .item__name small{text-transform:none}
.plain-line{font-weight:700;font-size:14.5px;line-height:16px;text-transform:uppercase;margin-bottom:8px}
.list-row{display:flex;align-items:baseline;font-size:14.5px;line-height:20px;font-weight:500}
.list-row__dots{flex:1;border-bottom:1px dotted var(--ink);margin:0 4px 0 2px;transform:translateY(-4px)}
.list-row__price{width:22px;text-align:right}
.gin .list-row{font-size:13px}
.events{position:absolute;left:0;top:1137px;width:850px;height:66px;background:var(--band)}
.events__label{position:absolute;left:36px;top:1143px;font-family:var(--serif);color:#f6d589;font-size:18px;line-height:16px;text-align:center}
.event{position:absolute;top:1119px;width:108px;height:69px;background:var(--tile);text-align:center;font-family:var(--serif)}
.event__day{display:block;font-size:13.5px;color:var(--ink);line-height:18px}
.event__icon{display:block;margin:2px auto 0;width:30px;height:28px}
.event__name{display:block;font-size:11.5px;color:var(--gold);line-height:13px}
</style>
</head>
<body>
<main class="menu">
  <div class="menu__backdrop" role="img" aria-label="Darkened photograph of the pub's bar interior behind the menu"></div>

  <div class="brand"><span class="brand__dot"></span><span class="brand__name">Tinker's Fox</span></div>

  <section class="section" style="left:34px;top:96px;width:382px;height:446px">
    <h2 class="section__title">BURGERS AND SANDWICHES</h2>
    <div class="item"><p class="item__name">Chicken Sandwich...$12</p><p class="item__desc">Chicken Breast, Applewood Bacon, Butter Lettuce, White Cheddar,<br>Avocado and Tomato Served on Sourdough Bread</p></div>
    <div class="item"><p class="item__name">Buttermilk Fried Chicken...$13</p><p class="item__desc">Coleslaw, Provolone, Tomato, and a Spiced Mayonnaise on a Pretzel Roll</p></div>
    <div class="item"><p class="item__name">Short Rib Sandwich...$13</p><p class="item__desc">Beef Shorts, Mayo, Tomato, Caramelized Onions, Arugula, Pepper Jack<br>Cheese Served on Sourdough Bread</p></div>
    <div class="item"><p class="item__name">Grilled Cheese Sandwich...$10</p><p class="item__desc">Cheese, Provolone and Cheddar Cheese</p></div>
    <div class="item"><p class="item__name">Tinker's Fox Burger...$14</p><p class="item__desc">Sharp Cheddar, Arugula, Roasted Shallots, Bacon Jam with Malt Aioli</p></div>
    <div class="item"><p class="item__name">The Truffle Burger...$15</p><p class="item__desc">Caramelized Onions, Arugula, Truffle Pecorino, Truffle Mayo and Truffle<br>Fries</p></div>
    <div class="item"><p class="item__name">The Sloppy Joe..$10</p><p class="item__desc">Shredded Lettuce and Sharp Cheddar</p></div>
    <div class="item"><p class="item__name">Veggie Burger...$12</p><p class="item__desc">Concoction of kale, Tomato, Avocado, Sharp Cheddar with a Balsamic<br>Reduction</p></div>
    <div class="item"><p class="item__name">Flat Iron Steak Sandwich...$16</p><p class="item__desc">Arugula, Peppers, Fontina, Onion and Mayo</p></div>
    <div class="item"><p class="item__name">Chicken Spinach Wrap...$10</p><p class="item__desc">Chicken, Bacon, Lettuce, Tomato, Avocado, Ranch and Mayo</p></div>
    <div class="item"><p class="item__name">Fried Chicken Sliders (4)...$12</p><p class="item__desc">Coleslaw, Lime Sriracha Sauce</p></div>
  </section>

  <section class="section upper" style="left:34px;top:568px;width:382px;height:237px">
    <h2 class="section__title">COCKTAILS</h2>
    <div class="item"><p class="item__name">Halloway's Tinker <small>(served Up)</small></p><p class="item__desc">Rye, cherry liqueur, lime, grapefruit ....11.</p></div>
    <div class="item"><p class="item__name">Build a Buck <small>(served over ice)</small></p><p class="item__desc">Vodka, tequila, gin or whiskey, lime, ginger beer ....10.</p></div>
    <div class="item"><p class="item__name">The Inside Job <small>(served Up)</small></p><p class="item__desc">Bourbon, absinthe, maraschino, aromatic bitters ....11.</p></div>
    <div class="item"><p class="item__name">Brazil vs Mexico <small>(served over ice)</small></p><p class="item__desc">Mezcal, Cachaca, Jalapeno, Fresh Lime Juice, Syrup....11.</p></div>
    <div class="item"><p class="item__name">Shishito Whiskey Sour <small>(served over ice)</small></p><p class="item__desc">Kiyora Whiskey, Fresh Lime, Shishito Pepper ....11.</p></div>
    <div class="item"><p class="item__name">Perra de Jalisco <small>(served Up)</small></p><p class="item__desc">Mezcal, lime, agave, cayenne ....11.</p></div>
  </section>

  <section class="section" style="left:34px;top:832px;width:382px;height:113px;padding-top:22px">
    <h2 class="section__title">BEER COCKTAILS ....9.</h2>
    <p class="plain-line">Snakebite - “Beer &amp; Cider”</p>
    <p class="plain-line" style="line-height:14px">Dogbite - “Beer, Lemonade<br>&amp; Sparkling Wine”</p>
    <p class="plain-line">Shandygaff - “Beer &amp; Ginger Beer”</p>
  </section>

  <section class="section upper" style="left:34px;top:968px;width:382px;height:131px;padding-top:20px">
    <h2 class="section__title">HAPPY HOUR ....6.</h2>
    <p class="item__desc" style="margin:-10px 0 6px">3 - 7 Daily</p>
    <div class="item"><p class="item__name">Lychee Grapefruit Margarita</p><p class="item__desc">Grapefruit Tequila, lychee puree</p></div>
    <div class="item"><p class="item__name">Moscow Mule</p><p class="item__desc">Vodka, lime, ginger beer</p></div>
    <div class="item"><p class="item__name">Old Fashioned</p><p class="item__desc">Bourbon, simple, bitters</p></div>
  </section>

  <section class="section" style="left:447px;top:96px;width:377px;height:244px;padding-top:26px">
    <h2 class="section__title">BIG DOG BITES</h2>
    <div class="item" style="margin-bottom:12px"><p class="item__name">Atlantic Cod Fish N' Chips...$15</p><p class="item__desc">House Tartar Sauce, Vinegar and Lemon Wedge</p></div>
    <div class="item" style="margin-bottom:12px"><p class="item__name">Oven Roasted ½ Roasted Chicken...$16</p><p class="item__desc">Boneless Chicken, Broccolini, Fingerling Potatoes, Topped with<br>Chimichurri Sauce</p></div>
    <div class="item" style="margin-bottom:12px"><p class="item__name">Black Mussels...$17</p><p class="item__desc">Tequila Chipotle Sauce, Cilantro and Cherry Tomatoes</p></div>
    <div class="item" style="margin-bottom:12px"><p class="item__name">Pan Seared Salmon...$19</p><p class="item__desc">Sushi Grade Salmon, Spaghetti Squash, Zucchini, Cherry Tomatoes In<br>a Lemon Caper Beurre Blanc</p></div>
    <div class="item"><p class="item__name">Flat Iron Steak...$22</p><p class="item__desc">French Fries, Baby Arugula in a Light peppercorn Sauce</p></div>
  </section>

  <section class="section" style="left:447px;top:360px;width:377px;height:240px">
    <h2 class="section__title">FLATBREADS</h2>
    <div class="item"><p class="item__name">Margherita...$12</p><p class="item__desc">Fresh Mozzarella, Roma Tomatoes and Fresh Italian Basil</p></div>
    <div class="item"><p class="item__name">Vegetarian...$13</p><p class="item__desc">Brussel Sprouts, Peppers, Onions, Zucchini, Goat Cheese, Smoked<br>Mozzarella Topped with a Balsamic Reduction</p></div>
    <div class="item"><p class="item__name">Prosciutto &amp; Arugula..$14</p><p class="item__desc">Red Onion, Parmesan, Mozzarella</p></div>
    <div class="item"><p class="item__name">Portobello &amp; Truffle...$14</p><p class="item__desc">Portobello White Mushroom, Fontina, Drizzled with Truffle Oil</p></div>
    <div class="item"><p class="item__name">Chicken Tikka Masala...$14</p><p class="item__desc">Tandoori Chicken, Fontini and Raita</p></div>
    <div class="item"><p class="item__name">The Tinker's Fox...$15</p><p class="item__desc">Meatballs, Sausage, Chorizo, Mozzarella and Fresen</p></div>
  </section>

  <section class="section" style="left:447px;top:622px;width:377px;height:95px;padding-top:24px">
    <h2 class="section__title">BRUNCH</h2>
    <p class="plain-line" style="line-height:15px;margin-bottom:10px">Mimosa ....8. / Bottle Sparkling Wine<br>+ OJ ....18.</p>
    <p class="plain-line">Michelada ....8. / Bottomless ....18.</p>
  </section>

  <section class="section" style="left:447px;top:738px;width:377px;height:146px;padding:16px 16px 0 26px">
    <h2 class="section__title">VODKA</h2>
    <div class="list-row"><span>BELLMOOR - rye -Poland</span><span class="list-row__dots"></span><span class="list-row__price">12</span></div>
    <div class="list-row"><span>KETTLE MARK - wheat - Holland</span><span class="list-row__dots"></span><span class="list-row__price">10</span></div>
    <div class="list-row"><span>GREY HERON - wheat - France</span><span class="list-row__dots"></span><span class="list-row__price">12</span></div>
    <div class="list-row"><span>TOMÁS'S - corn - Texas</span><span class="list-row__dots"></span><span class="list-row__price">10</span></div>
    <div class="list-row"><span>SKERRY - wheat &amp; barley - Iceland</span><span class="list-row__dots"></span><span class="list-row__price">9</span></div>
    <div class="list-row"><span>CHAPELLE - Potato - Poland</span><span class="list-row__dots"></span><span class="list-row__price">10</span></div>
  </section>

  <section class="section gin" style="left:447px;top:905px;width:377px;height:195px;padding:13px 16px 0 26px">
    <h2 class="section__title">GIN</h2>
    <div class="list-row"><span>BIRCH HOLLOW (honey) - Vermont</span><span class="list-row__dots"></span><span class="list-row__price">13</span></div>
    <div class="list-row"><span>KEEL GIN - California</span><span class="list-row__dots"></span><span class="list-row__price">11</span></div>
    <div class="list-row"><span>BAYPORT - London Dry - England</span><span class="list-row__dots"></span><span class="list-row__price">9</span></div>
    <div class="list-row"><span>BAYPORT AZURE - London Dry - England</span><span class="list-row__dots"></span><span class="list-row__price">11</span></div>
    <div class="list-row"><span>HADLEY'S (rose &amp; cucumber) - Scotland</span><span class="list-row__dots"></span><span class="list-row__price">12</span></div>
    <div class="list-row"><span>OXMOOR England</span><span class="list-row__dots"></span><span class="list-row__price">13</span></div>
    <div class="list-row"><span>ST. LORNE - “Herbarist” California</span><span class="list-row__dots"></span><span class="list-row__price">11</span></div>
    <div class="list-row"><span>TANNERBY - London Dry England</span><span class="list-row__dots"></span><span class="list-row__price">10</span></div>
    <div class="list-row"><span>THE GLEANER -“22”-Islay Dry - Scotland</span><span class="list-row__dots"></span><span class="list-row__price">11</span></div>
  </section>

  <div class="events"></div>
  <p class="events__label">EVENT<br>SCHEDULE</p>

  <div class="event" style="left:165px"><span class="event__day">Monday</span>
    <svg class="event__icon" viewBox="0 0 30 28" fill="none" stroke="#f2a51f" stroke-width="2"><circle cx="15" cy="14" r="11"/><circle cx="15" cy="14" r="6"/></svg>
    <span class="event__name">Beer Pong</span></div>
  <div class="event" style="left:299px"><span class="event__day">Tuesday</span>
    <svg class="event__icon" viewBox="0 0 30 28" fill="none" stroke="#f2a51f" stroke-width="2"><circle cx="15" cy="14" r="11"/><path d="M11.5 11a3.5 3.5 0 1 1 5 3c-1.2.6-1.5 1.3-1.5 2.5"/><circle cx="15" cy="20" r=".8" fill="#f2a51f"/></svg>
    <span class="event__name">Trivia</span></div>
  <div class="event" style="left:432px"><span class="event__day">Wednesday</span>
    <svg class="event__icon" viewBox="0 0 30 28" fill="none" stroke="#f2a51f" stroke-width="2"><path d="M4 21a11 11 0 0 1 22 0z"/></svg>
    <span class="event__name">Taco</span></div>
  <div class="event" style="left:566px"><span class="event__day">Thursday</span>
    <svg class="event__icon" viewBox="0 0 30 28" fill="none" stroke="#f2a51f" stroke-width="2"><path d="M8 4h14l-2 20H10z"/><path d="M9 13h12"/></svg>
    <span class="event__name">Whiskey</span></div>
  <div class="event" style="left:699px"><span class="event__day">Friday</span>
    <svg class="event__icon" viewBox="0 0 30 28" fill="none" stroke="#f2a51f" stroke-width="2"><circle cx="19" cy="9" r="6"/><path d="M15 13 5 24"/></svg>
    <span class="event__name">Karaoke</span></div>
</main>
</body>
</html>
```